Hello,

I would like to recieve a template that i can use for:

Presentation folders
pdf files
word files

Logo, fond and colors are included in attachment.

Target Market(s)

Small Business

Requirements
Must have
• clean and simple

```html
<!DOCTYPE html>
<html lang="en">
<head>
<meta charset="utf-8">
<title>Taskwell Stationery Set</title>
<link href="https://fonts.googleapis.com/css2?family=Mulish:wght@400;600&display=swap" rel="stylesheet">
<style>
  :root {
    --bg: #ececec;
    --paper: #f4f4f4;
    --blue: #1fa3e0;
    --green: #7ab52a;
    --ink: #3a3a3a;
    --ghost: #dadada;
    --font: "Mulish", "Helvetica Neue", Arial, sans-serif;
  }
  * { margin: 0; padding: 0; box-sizing: border-box; }
  html, body { width: 1200px; height: 795px; overflow: hidden; }
  body { background: var(--bg); font-family: var(--font); color: var(--ink); position: relative; }

  .sheet { position: absolute; background: var(--paper); overflow: hidden; box-shadow: 0 1px 3px rgba(0,0,0,.12); }

  .brand { position: absolute; display: flex; align-items: center; }
  .brand-mark { background: var(--blue); border-radius: 3px; margin-right: 4px; }
  .brand-name { color: var(--green); font-weight: 600; line-height: 1; }

  .ghost-mark { position: absolute; background: var(--ghost); border-radius: 14px; }

  .footer-bands { position: absolute; left: 0; right: 0; bottom: 0; }
  .band-green { height: 5px; background: var(--green); width: 60%; }
  .band-blue { background: var(--blue); color: #fff; font-size: 6px; display: flex; align-items: center; justify-content: flex-end; padding-right: 18px; }

  .contact { position: absolute; font-size: 5.5px; line-height: 1.35; }
  .contact b { color: var(--blue); font-weight: 600; }

  /* Letterhead */
  .letterhead { left: 292px; top: 99px; width: 293px; height: 415px; }
  .letterhead .band-blue { height: 14px; }

  /* Folder */
  .folder { left: 635px; top: 80px; width: 347px; height: 437px; border-left: 6px solid #e4e4e4; }

  /* Business cards */
  .card { left: 187px; width: 131px; }
  .card-back { top: 551px; height: 74px; }
  .card-front { top: 647px; height: 77px; }
  .card .band-blue { height: 4px; }
  .card .band-green { height: 2px; }
  .card-back .card-details { left: 9px; top: 36px; font-size: 4.2px; line-height: 1.15; }
  .card-back .card-person { right: 9px; top: 37px; font-size: 4.2px; line-height: 1.15; text-align: right; }

  /* Compliment slip */
  .slip { left: 353px; top: 563px; width: 325px; height: 160px; }
  .slip .band-blue { height: 12px; }

  /* Envelope */
  .envelope { left: 712px; top: 562px; width: 330px; height: 162px; }
  .envelope svg { position: absolute; left: 0; top: 0; }
  .seal { position: absolute; left: 159px; top: 12px; width: 14px; height: 18px; background: #111; border-radius: 2px; }
</style>
</head>
<body>

  <!-- Letterhead -->
  <section class="sheet letterhead">
    <div class="brand" style="left:28px;top:18px;">
      <span class="brand-mark" style="width:22px;height:22px;"></span>
      <span class="brand-name" style="font-size:22px;">Taskwell</span>
    </div>
    <div class="contact" style="left:209px;top:28px;">
      <div><b>P</b> 123-555-0148</div>
      <div><b>E</b> info@taskwell.co</div>
      <div><b>W</b> www.taskwell.co</div>
    </div>
    <div class="ghost-mark" style="left:194px;top:202px;width:120px;height:110px;"></div>
    <div class="footer-bands">
      <div class="band-green" style="width:68%;"></div>
      <div class="band-blue">Maple Lane Riverton NY 12345</div>
    </div>
  </section>

  <!-- Presentation folder -->
  <section class="sheet folder">
    <div class="brand" style="left:52px;top:86px;">
      <span class="brand-mark" style="width:58px;height:58px;border-radius:6px;margin-right:10px;"></span>
      <span class="brand-name" style="font-size:46px;">Taskwell</span>
    </div>
    <div class="ghost-mark" style="left:160px;top:212px;width:186px;height:188px;border-radius:20px;"></div>
  </section>

  <!-- Business card: contact side -->
  <section class="sheet card card-back">
    <div class="brand" style="left:9px;top:9px;">
      <span class="brand-mark" style="width:12px;height:12px;border-radius:2px;margin-right:3px;"></span>
      <span class="brand-name" style="font-size:12px;">Taskwell</span>
    </div>
    <div class="contact card-details">
      <div>Maple Lane</div>
      <div>Riverton NY 12345</div>
      <div style="margin-top:1px;"><b>P</b> 123-555-0148</div>
      <div><b>E</b> info@taskwell.co</div>
      <div><b>W</b> www.taskwell.co</div>
    </div>
    <div class="contact card-person">
      <div style="color:var(--blue);font-weight:600;">Employee Name</div>
      <div style="color:var(--green);">Position Title</div>
    </div>
    <div class="footer-bands">
      <div class="band-green" style="width:65%;"></div>
      <div class="band-blue"></div>
    </div>
  </section>

  <!-- Business card: brand side -->
  <section class="sheet card card-front">
    <div class="brand" style="left:17px;top:24px;">
      <span class="brand-mark" style="width:20px;height:20px;margin-right:4px;"></span>
      <span class="brand-name" style="font-size:19px;">Taskwell</span>
    </div>
    <div class="contact" style="left:0;right:0;top:56px;text-align:center;font-size:4.5px;color:var(--blue);">www.taskwell.co</div>
  </section>

  <!-- Compliment slip -->
  <section class="sheet slip">
    <div class="brand" style="left:12px;top:20px;">
      <span class="brand-mark" style="width:26px;height:26px;margin-right:5px;"></span>
      <span class="brand-name" style="font-size:23px;">Taskwell</span>
    </div>
    <div class="ghost-mark" style="left:265px;top:28px;width:70px;height:88px;border-radius:10px;"></div>
    <div class="footer-bands">
      <div class="band-green" style="width:68%;"></div>
      <div class="band-blue">Maple Lane Riverton NY 12345</div>
    </div>
  </section>

  <!-- Envelope -->
  <section class="sheet envelope">
    <svg width="330" height="162" viewBox="0 0 330 162" aria-hidden="true">
      <path d="M1 2 L8 48 Q10 54 18 54 L312 54 Q320 54 322 48 L329 2" fill="none" stroke="#c8c8c8" stroke-width="1"/>
    </svg>
    <span class="seal"></span>
  </section>

</body>
</html>
```